Business Card Re-Design for a Lighting Designer

I would like my business card re-designed. It is currently high gloss and they scratch too easily. I don not think the current design lends itself well to a matte finish. I have included the current design for reference along with our company logo.
Check out our website for current branding.
http://www.brenmoorastudio.example

Updates
Some of the top contenders are muslim and it is a holiday for them. I do not want to discriminate and would expect the same courtesy for holidays we celebrate.
Target Market(s)
Interior Designers, Architects
Contact Information for Business Card
Logo - Name, Title, Address, Telephone Number and Extension, Email
Font styles to use
Requirements
Must have
- All the information listed on the current business card. If you use Red, it needs to be the red from our logo.
Nice to have
- Vertical and Horizontal Designs will be entertained.
Should not have
- Requirements for a glossy finish...should not look too corporate since we are a design firm.

```html
<!DOCTYPE html>
<html lang="en">
<head>
<meta charset="utf-8">
<title>Brenmoora Studio – Business Card</title>
<link rel="stylesheet" href="https://fonts.googleapis.com/css2?family=Josefin+Sans:wght@300;400&family=Open+Sans:wght@400;800&display=swap">
<style>
  :root {
    --brand-red: #a62b22;
    --brand-red-deep: #9b1816;
    --brand-red-soft: #a8302a;
    --ink: #1a1a1a;
    --paper: #ffffff;
    --blush: #f5e4de;
    --blush-light: #fbf1ed;
    --tagline: #9a8680;
    --rule: #c98a72;
    --white: #ffffff;
  }
  * { margin: 0; padding: 0; box-sizing: border-box; }
  html, body { width: 1200px; height: 1000px; overflow: hidden; background: var(--paper); }
  body { position: relative; font-family: "Josefin Sans", sans-serif; }

  .card { position: absolute; width: 428px; height: 662px; overflow: hidden; }
  .card-front { left: 113px; top: 169px; background: var(--brand-red); }
  .card-back { left: 635px; top: 172px; background: var(--blush); border: 1px solid var(--brand-red); }
  .card-planes { position: absolute; inset: 0; width: 100%; height: 100%; }

  .wordmark {
    position: absolute;
    font-family: "Josefin Sans", sans-serif;
    font-weight: 300;
    line-height: 1.05;
    letter-spacing: 0.01em;
  }
  .wordmark-mark { display: block; width: 44px; height: 44px; margin-bottom: 14px; }
  .card-front .wordmark { left: 124px; top: 86px; color: var(--ink); font-size: 34px; }
  .card-front .wordmark-mark { background: var(--ink); }
  .card-back .wordmark { left: 140px; top: 182px; color: var(--brand-red-deep); font-size: 34px; }
  .card-back .wordmark-mark { background: var(--brand-red-deep); }

  .tagline {
    position: absolute; left: 140px; top: 362px; width: 167px;
    border-top: 2px solid var(--rule);
    padding-top: 5px;
    font-family: "Open Sans", sans-serif; font-size: 9.5px;
    letter-spacing: 0.08em; color: var(--tagline); white-space: nowrap;
  }

  .person-name {
    position: absolute; left: 68px; top: 396px;
    font-family: "Open Sans", sans-serif; font-weight: 800;
    font-size: 34px; color: var(--ink); letter-spacing: -0.01em;
  }
  .person-title {
    position: absolute; left: 72px; top: 438px;
    font-family: "Open Sans", sans-serif; font-size: 18px; color: var(--white);
  }
  .contact-list { position: absolute; left: 68px; top: 476px; list-style: none; }
  .contact-item {
    display: flex; align-items: center; height: 32px;
    font-size: 17px; font-weight: 300; color: var(--white);
  }
  .contact-icon { width: 24px; height: 24px; margin-right: 9px; flex: none; }

  .address {
    position: absolute; left: 10px; right: 10px; top: 600px;
    font-size: 17px; font-weight: 300; color: var(--ink); text-align: center; line-height: 1.35;
  }
  .address-line { display: flex; align-items: center; justify-content: center; }
  .address-icon { width: 24px; height: 24px; margin-right: 8px; flex: none; }
</style>
</head>
<body>

<section class="card card-front" aria-label="Card front">
  <svg class="card-planes" viewBox="0 0 428 662" aria-hidden="true">
    <polygon points="0,0 428,0 428,127 0,265" fill="var(--brand-red-deep)"/>
    <polygon points="145,0 428,0 401,87" fill="var(--brand-red-soft)"/>
  </svg>

  <div class="wordmark">
    <span class="wordmark-mark"></span>
    BRENMOORA<br>STUDIO
  </div>

  <h1 class="person-name">MAREN OLVEY</h1>
  <p class="person-title">PRINCIPAL</p>

  <ul class="contact-list">
    <li class="contact-item">
      <svg class="contact-icon" viewBox="0 0 24 24" aria-hidden="true">
        <rect width="24" height="24" fill="var(--ink)"/>
        <rect x="4" y="6.5" width="16" height="11" fill="none" stroke="#fff" stroke-width="1.6"/>
        <polyline points="4,6.5 12,13 20,6.5" fill="none" stroke="#fff" stroke-width="1.6"/>
      </svg>
      maren@brenmoorastudio.example
    </li>
    <li class="contact-item">
      <svg class="contact-icon" viewBox="0 0 24 24" aria-hidden="true">
        <rect width="24" height="24" fill="var(--ink)"/>
        <circle cx="12" cy="12" r="7.5" fill="none" stroke="#fff" stroke-width="1.4"/>
        <ellipse cx="12" cy="12" rx="3.2" ry="7.5" fill="none" stroke="#fff" stroke-width="1.2"/>
        <line x1="4.5" y1="12" x2="19.5" y2="12" stroke="#fff" stroke-width="1.2"/>
      </svg>
      www.brenmoorastudio.example
    </li>
    <li class="contact-item">
      <svg class="contact-icon" viewBox="0 0 24 24" aria-hidden="true">
        <rect width="24" height="24" fill="var(--ink)"/>
        <path d="M7 5 l3 0 l1 4 l-2 1.5 q1.5 3 4.5 4.5 l1.5 -2 l4 1 l0 3 q-1 1.5 -3 1.5 q-6 -1 -10 -8 q-0.5 -3 1 -5.5z" fill="#fff"/>
      </svg>
      555.014.2280 X1
    </li>
  </ul>
</section>

<section class="card card-back" aria-label="Card back">
  <svg class="card-planes" viewBox="0 0 428 662" aria-hidden="true">
    <polygon points="0,0 428,0 428,126 0,266" fill="var(--white)"/>
    <polygon points="145,0 426,6 398,86" fill="var(--blush-light)"/>
  </svg>

  <div class="wordmark">
    <span class="wordmark-mark"></span>
    BRENMOORA<br>STUDIO
  </div>
  <p class="tagline">LIGHTING FOR ARCHITECTURE</p>

  <address class="address" style="font-style: normal;">
    <span class="address-line">
      <svg class="address-icon" viewBox="0 0 24 24" aria-hidden="true">
        <rect width="24" height="24" fill="var(--brand-red-deep)"/>
        <path d="M12 4.5 a5.5 5.5 0 0 1 5.5 5.5 c0 4 -5.5 9.5 -5.5 9.5 s-5.5 -5.5 -5.5 -9.5 a5.5 5.5 0 0 1 5.5 -5.5z" fill="#fff"/>
        <circle cx="12" cy="10" r="2" fill="var(--brand-red-deep)"/>
      </svg>
      612 Corwin Mill Parkway, Suite 140 Halden,
    </span>
    Georgia 30999 USA
  </address>
</section>

</body>
</html>
```